Fennimore Glen Books -- young adult, fantasy for small publisher looking for long term relationship fo

THE GLASS TOWER.
YA fantasy. Tolin, black hair, grey eyes, lives alone in a decaying red metropolis. Alone that is except for the body drifting slowly to shore and the shadows who look after him, tutor him, etc. He will have to fight against a non-human army if he is to win his way off the island and THE GLASS TOWER.
AUTHOR -- JOSEPH R. QUINTON
SERIES -- CHRONICLE OF THE HOLLOW PEAKS
book size -- 5 x 8

Target Market(s)

Age 12+ boys, adults who read fantasy

Industry/Entity Type

Book Publisher

Requirements
Must have
• red city in background, boy's face -- black hair, grey eyes, sea (if possible). I need something that will POP on North American bookshelves, something that will scream out BUY ME BUY ME!!!

```html
<!DOCTYPE html>
<html lang="en">
<head>
<meta charset="utf-8">
<title>The Glass Tower — Cover Wrap</title>
<link rel="stylesheet" href="https://fonts.googleapis.com/css2?family=Saira:ital,wght@1,900&family=Exo+2:wght@600;700&family=Montserrat:wght@400;600&display=swap">
<style>
  :root {
    --bg: #ececec;
    --red: #c8161b;
    --red-deep: #8e0d12;
    --red-dark: #6e0a0e;
    --silver-light: #f4f4f4;
    --silver-dark: #9a9a9a;
    --gold: #e2a51c;
    --paper: #f1efea;
    --ink: #1c1c1c;
    --body-text: #3a0608;
  }
  * { margin: 0; padding: 0; box-sizing: border-box; }
  html, body { width: 1200px; height: 800px; overflow: hidden; background: var(--bg); }
  .cover-wrap {
    position: absolute; left: 170px; top: 80px;
    width: 860px; height: 640px;
    display: flex;
    box-shadow: 0 18px 40px rgba(0,0,0,.25);
  }
  .back-cover, .front-cover {
    width: 400px; height: 640px; position: relative; overflow: hidden;
  }
  .back-cover {
    background: radial-gradient(ellipse at 50% 40%, var(--red) 0%, var(--red-deep) 75%, var(--red-dark) 100%);
    padding: 34px 28px 0;
    text-align: center;
  }
  .spine {
    width: 60px; height: 640px;
    background: linear-gradient(90deg, var(--red-deep), var(--red) 50%, var(--red-deep));
    display: flex; flex-direction: column; align-items: center;
    padding: 24px 0;
    gap: 26px;
  }
  .front-cover {
    background: var(--red);
  }
  .title-the, .title-main {
    font-family: "Saira", sans-serif; font-weight: 900; font-style: italic;
    background: linear-gradient(160deg, var(--silver-light) 0%, #ffffff 30%, var(--silver-dark) 45%, var(--silver-light) 60%, #cfcfcf 100%);
    -webkit-background-clip: text; background-clip: text; color: transparent;
    line-height: 1;
  }
  .title-the { font-size: 38px; letter-spacing: 1px; }
  .title-main { font-size: 50px; letter-spacing: -1px; white-space: nowrap; }
  .series {
    font-family: "Exo 2", sans-serif; font-weight: 700;
    color: var(--gold); font-size: 13px; letter-spacing: 3px;
    margin-top: 8px; white-space: nowrap;
  }
  .blurb {
    margin-top: 20px;
    font-family: "Montserrat", sans-serif; font-size: 10.5px; line-height: 1.52;
    color: var(--body-text); text-align: justify;
  }
  .back-boxes {
    position: absolute; left: 28px; right: 28px; bottom: 30px;
    display: flex; justify-content: space-between;
  }
  .placeholder-box {
    width: 112px; height: 66px; background: var(--red);
    box-shadow: inset 0 0 0 1px rgba(255,255,255,.08);
    display: flex; align-items: center; justify-content: center;
    font-family: "Montserrat", sans-serif; font-size: 9px; color: #f3d9d9;
  }
  .spine-title {
    writing-mode: vertical-rl;
    font-family: "Saira", sans-serif; font-weight: 900; font-style: italic;
    font-size: 30px; color: var(--silver-light); letter-spacing: 1px; white-space: nowrap;
  }
  .spine-author {
    writing-mode: vertical-rl;
    background: var(--paper); color: var(--ink);
    font-family: "Exo 2", sans-serif; font-weight: 700; font-size: 11px; letter-spacing: 3px;
    padding: 10px 4px; white-space: nowrap;
  }
  .city-art {
    position: absolute; left: 0; top: 0; width: 400px; height: 300px;
  }
  .front-title {
    position: absolute; left: 0; right: 0; top: 350px; text-align: center;
  }
  .front-title .title-the { font-size: 42px; }
  .front-title .title-main { font-size: 54px; }
  .author-plate {
    display: inline-block; margin-top: 16px;
    background: var(--paper); color: var(--ink);
    font-family: "Exo 2", sans-serif; font-weight: 700; font-size: 13px; letter-spacing: 3px;
    padding: 6px 12px;
  }
</style>
</head>
<body>
<main class="cover-wrap">
  <section class="back-cover">
    <div class="title-the">THE</div>
    <div class="title-main">GLASS TOWER</div>
    <div class="series">CHRONICLE OF THE HOLLOW PEAKS</div>
    <p class="blurb">Lorem ipsum dolor sit amet, consectetur adipisicing elit, sed do eiusmod tempor incididunt ut labore et dolore magna aliqua. Ut enim ad minim veniam, quis nostrud exercitation. Lorem ipsum dolor sit amet, consectetur adipisicing elit, sed do eiusmod tempor incididunt ut labore et dolore magna aliqua. Ut enim ad minim veniam, quis nostrud exercitation. Lorem ipsum dolor sit amet, consectetur adipisicing elit, sed do eiusmod tempor incididunt ut labore et dolore magna aliqua. Ut enim ad minim veniam, quis nostrud exercitation. Lorem ipsum dolor sit amet, consectetur adipisicing elit, sed do eiusmod tempor incididunt ut labore et dolore magna aliqua. Ut enim ad minim veniam, quis nostrud exercitation. Lorem ipsum dolor sit amet, consectetur adipisicing elit, sed do eiusmod tempor incididunt ut labore et dolore magna aliqua. Ut enim ad minim veniam, quis nostrud exercitation. Lorem ipsum dolor sit amet, consectetur adipisicing elit, sed do eiusmod tempor incididunt ut labore et dolore magna aliqua.</p>
    <div class="back-boxes">
      <div class="placeholder-box">LOGO</div>
      <div class="placeholder-box">ISBN</div>
    </div>
  </section>

  <section class="spine">
    <div class="spine-title">THE GLASS TOWER</div>
    <div class="spine-author">BY: JOSEPH R. QUINTON</div>
  </section>

  <section class="front-cover">
    <svg class="city-art" role="img" aria-label="Pale distressed skyline of a red city above the sea" viewBox="0 0 400 300" preserveAspectRatio="none">
      <defs>
        <linearGradient id="cityTone" x1="0" y1="0" x2="0" y2="1">
          <stop offset="0" stop-color="#d42a2e"/>
          <stop offset="0.35" stop-color="#e7c9c6"/>
          <stop offset="1" stop-color="#f1ece8"/>
        </linearGradient>
      </defs>
      <rect width="400" height="300" fill="url(#cityTone)"/>
      <rect y="285" width="400" height="15" fill="#f6f3ef"/>
    </svg>
    <div class="front-title">
      <div class="title-the">THE</div>
      <div class="title-main">GLASS TOWER</div>
      <div class="series">CHRONICLE OF THE HOLLOW PEAKS</div>
      <div class="author-plate">BY: JOSEPH R. QUINTON</div>
    </div>
  </section>
</main>
</body>
</html>
```